Brightpath Dentistry - Flyer - Modern & Eye catching campaign flyer

Need front & back side full page flyer designs for both 1) Grand opening 2) On-going campaign.

Attached the new dental office logo.
Attached our other dental clinic flyer designs for content.

Target Market(s)

Cosmetic dentistry

Industry/Entity Type

Health Care

Requirements
Must have
• decent, modern and eye catching marketing flyers.
Nice to have
• - Nice space
• - Highlight phone number
• - Highlight special features like convenient hours, call or text, for all ages, digital facility, etc
Should not have
• - Don't want to fill the flyer with too much wordings
• - Too many colors

```html
<!DOCTYPE html>
<html lang="en">
<head>
<meta charset="utf-8">
<title>Brightpath Dentistry – Services Flyer</title>
<link href="https://fonts.googleapis.com/css2?family=Titillium+Web:wght@300;400;600;700&family=PT+Serif:wght@700&display=swap" rel="stylesheet">
<style>
  :root {
    --navy: #27548f;
    --frame: #1b2a44;
    --cyan: #29b6e6;
    --cyan-bright: #1fc0e6;
    --header-cyan: #0fb3d8;
    --orange: #f7941d;
    --white: #ffffff;
    --ink: #27548f;
  }
  * { margin: 0; padding: 0; box-sizing: border-box; }
  html, body { width: 875px; height: 1200px; overflow: hidden; background: var(--navy); }
  .flyer {
    position: relative; width: 875px; height: 1200px; overflow: hidden;
    background: var(--navy);
    font-family: "Titillium Web", sans-serif; color: var(--white);
  }
  .flyer-frame {
    position: absolute; left: 11px; top: 0; right: 11px; bottom: 11px;
    border: 1.5px solid var(--frame); border-top: none; pointer-events: none;
  }
  .header-band { position: absolute; left: 0; top: 0; width: 875px; height: 190px; }
  .brand {
    position: absolute; left: 0; right: 0; top: 46px; text-align: center;
    color: var(--header-cyan); font-weight: 700; line-height: 1;
  }
  .brand-mark {
    display: inline-block; width: 14px; height: 14px; border-radius: 50%;
    background: var(--header-cyan); vertical-align: middle; margin-right: 14px;
  }
  .brand-name { font-size: 46px; letter-spacing: 1px; vertical-align: middle; }

  .services {
    position: absolute; left: 105px; top: 271px; width: 668px; height: 385px;
    border: 1.5px solid var(--cyan); border-radius: 22px;
    box-shadow: 0 14px 18px -12px rgba(10,30,60,.55);
  }
  .services-title {
    position: absolute; left: 0; right: 0; top: 238px; text-align: center;
    font-size: 52px; font-weight: 700; color: var(--orange); line-height: 1;
  }
  .services-title-mask {
    position: absolute; left: 222px; top: 260px; width: 430px; height: 20px; background: var(--navy);
  }
  .title-dot { position: absolute; top: 265px; width: 12px; height: 12px; border-radius: 50%; background: var(--cyan); }
  .divider { position: absolute; width: 1.5px; height: 64px; background: var(--white); }
  .service-icon {
    position: absolute; width: 62px; height: 50px; margin-left: -31px;
    background: linear-gradient(180deg, #ffffff, #dfe9f3); border-radius: 10px;
  }
  .service-label {
    position: absolute; width: 200px; margin-left: -100px; text-align: center;
    font-size: 10.5px; font-weight: 700; color: var(--cyan); line-height: 1.35; letter-spacing: .2px;
  }

  .offer-bar {
    position: absolute; height: 45px; background: var(--white);
    clip-path: polygon(30px 0, 100% 0, 100% 100%, 30px 100%, 0 50%);
    color: var(--ink); font-size: 24px; font-weight: 400; line-height: 45px;
    text-align: right; padding-right: 24px;
  }
  .offer-price {
    position: absolute; left: 744px; width: 131px; height: 64px;
    background: var(--cyan-bright);
    clip-path: polygon(18px 0, 100% 0, 100% 100%, 18px 100%, 0 50%);
    font-family: "PT Serif", serif; font-weight: 700; font-size: 42px; line-height: 64px;
    padding-left: 26px; color: var(--white);
  }
  .offer-note {
    position: absolute; right: 146px; font-size: 12px; color: var(--orange); letter-spacing: .2px;
  }
  .offer-includes span { margin-left: 6px; }
  .tick { width: 11px; height: 11px; vertical-align: -1px; margin-right: 2px; }

  .hours { position: absolute; left: 48px; top: 785px; width: 320px; height: 185px; }
  .hours-arc { position: absolute; left: 0; top: 0; }
  .hours-title {
    position: absolute; left: 0; right: 0; top: 40px; text-align: center;
    font-size: 24px; font-weight: 700; color: var(--orange); line-height: 1.3;
  }
  .hours-note { position: absolute; left: 0; right: 0; top: 104px; text-align: center; font-size: 12.5px; }
  .hours-welcome {
    position: absolute; left: 0; right: 0; top: 125px; text-align: center;
    font-size: 15.5px; font-weight: 700; color: var(--orange);
  }

  .cta-heading {
    position: absolute; left: 0; right: 0; top: 1054px; text-align: center;
    font-size: 26px; font-weight: 400; letter-spacing: .3px;
  }
  .phone-pill {
    position: absolute; left: 289px; top: 1096px; width: 350px; height: 61px;
    background: var(--orange); border-radius: 0 31px 31px 0;
    font-family: "PT Serif", serif; font-weight: 700; font-size: 48px; line-height: 61px;
    padding-left: 18px; color: var(--white); letter-spacing: -.5px;
    box-shadow: 2px 4px 6px rgba(10,30,60,.35);
  }
  .phone-badge {
    position: absolute; left: 221px; top: 1089px; width: 75px; height: 75px; border-radius: 50%;
    background: var(--white); border: 3px solid var(--navy);
    display: flex; align-items: center; justify-content: center;
  }
</style>
</head>
<body>
<main class="flyer">
  <svg class="header-band" viewBox="0 0 875 190" aria-hidden="true">
    <defs>
      <linearGradient id="headerFade" x1="0" x2="1" y1="0" y2="0">
        <stop offset="0" stop-color="#0fb3d8"/>
        <stop offset=".5" stop-color="#ffffff"/>
        <stop offset="1" stop-color="#0fb3d8"/>
      </linearGradient>
    </defs>
    <path d="M0 0 H875 V160 Q437 190 0 160 Z" fill="url(#headerFade)"/>
  </svg>
  <div class="brand"><span class="brand-mark"></span><span class="brand-name">Brightpath Dentistry</span></div>

  <div class="services"></div>
  <div class="services-title-mask"></div>
  <span class="title-dot" style="left:214px"></span>
  <span class="title-dot" style="left:642px"></span>
  <h1 class="services-title">OUR SERVICES</h1>

  <span class="divider" style="left:314px;top:332px"></span>
  <span class="divider" style="left:552px;top:332px"></span>
  <span class="divider" style="left:314px;top:452px"></span>
  <span class="divider" style="left:552px;top:452px"></span>
  <span class="divider" style="left:314px;top:553px"></span>
  <span class="divider" style="left:552px;top:553px"></span>

  <div class="service-icon" style="left:193px;top:318px" role="img" aria-label="Root canal tooth icon"></div>
  <div class="service-icon" style="left:436px;top:318px" role="img" aria-label="Dental implant icon"></div>
  <div class="service-icon" style="left:671px;top:318px" role="img" aria-label="Sparkling white tooth icon"></div>
  <div class="service-icon" style="left:193px;top:448px;height:32px" role="img" aria-label="Dentures icon"></div>
  <div class="service-icon" style="left:436px;top:446px;height:42px" role="img" aria-label="Crown and bridge icon"></div>
  <div class="service-icon" style="left:671px;top:440px;height:52px" role="img" aria-label="Night guard icon"></div>
  <div class="service-icon" style="left:193px;top:555px;height:48px" role="img" aria-label="Tooth extraction icon"></div>
  <div class="service-icon" style="left:436px;top:555px;height:54px" role="img" aria-label="Veneers icon"></div>
  <div class="service-icon" style="left:671px;top:561px;height:30px;width:76px;margin-left:-38px" role="img" aria-label="Clear aligners icon"></div>

  <p class="service-label" style="left:193px;top:389px">ROOT CANAL THERAPY</p>
  <p class="service-label" style="left:436px;top:390px">IMPLANTS</p>
  <p class="service-label" style="left:671px;top:392px">LUMAGLOW TEETH WHITENING</p>
  <p class="service-label" style="left:193px;top:507px">DENTURES</p>
  <p class="service-label" style="left:436px;top:507px">CROWN AND BRIDGE</p>
  <p class="service-label" style="left:671px;top:507px">NIGHT GUARDS</p>
  <p class="service-label" style="left:193px;top:622px">EXTRACTIONS</p>
  <p class="service-label" style="left:436px;top:622px">VENEERS</p>
  <p class="service-label" style="left:677px;top:614px">CLEARALIGN<br>(Invisible braces)</p>

  <div class="offer-bar" style="left:470px;top:723px;width:281px">New Patient Special</div>
  <div class="offer-price" style="top:714px">$59</div>
  <p class="offer-note offer-includes" style="top:773px">
    <svg class="tick" viewBox="0 0 12 12" aria-hidden="true"><circle cx="5" cy="7" r="4" fill="#ffffff"/><path d="M3 7l2 2 6-8" stroke="#f7941d" stroke-width="1.8" fill="none"/></svg>EXAM
    <span><svg class="tick" viewBox="0 0 12 12" aria-hidden="true"><circle cx="5" cy="7" r="4" fill="#ffffff"/><path d="M3 7l2 2 6-8" stroke="#f7941d" stroke-width="1.8" fill="none"/></svg>DIGITAL X-RAYS</span>
    <span><svg class="tick" viewBox="0 0 12 12" aria-hidden="true"><circle cx="5" cy="7" r="4" fill="#ffffff"/><path d="M3 7l2 2 6-8" stroke="#f7941d" stroke-width="1.8" fill="none"/></svg>CLEANING</span>
  </p>

  <div class="offer-bar" style="left:426px;top:822px;width:325px">In-Office Teeth Whitening</div>
  <div class="offer-price" style="top:812px">$249</div>
  <p class="offer-note" style="top:873px">(Reg Prices $500)</p>

  <div class="offer-bar" style="left:470px;top:926px;width:281px">Veneers / Lumivue</div>
  <div class="offer-price" style="top:917px">$695</div>
  <p class="offer-note" style="top:977px">(Reg Prices $995)</p>

  <section class="hours">
    <svg class="hours-arc" width="320" height="185" viewBox="0 0 320 185" aria-hidden="true">
      <path d="M86 40 A92 92 0 0 1 234 40" stroke="#ffffff" stroke-width="1.3" fill="none"/>
      <path d="M86 145 A92 92 0 0 0 234 145" stroke="#ffffff" stroke-width="1.3" fill="none"/>
    </svg>
    <h2 class="hours-title">CONVENIENT EVENING &amp;<br>SATURDAY HOURS</h2>
    <p class="hours-note">New Patients Only. Offer expires in 30 days.</p>
    <p class="hours-welcome">NEW PATIENTS ARE WELCOME !</p>
  </section>

  <p class="cta-heading">CALL or TEXT US NOW</p>
  <div class="phone-pill">610-555-0148</div>
  <div class="phone-badge">
    <svg width="40" height="40" viewBox="0 0 24 24" aria-hidden="true">
      <path d="M6.6 10.8c1.4 2.8 3.8 5.1 6.6 6.6l2.2-2.2c.3-.3.7-.4 1-.2 1.1.4 2.3.6 3.6.6.6 0 1 .4 1 1V20c0 .6-.4 1-1 1C10.6 21 3 13.4 3 4c0-.6.4-1 1-1h3.5c.6 0 1 .4 1 1 0 1.3.2 2.5.6 3.6.1.3 0 .7-.2 1z" fill="#27548f"/>
    </svg>
  </div>

  <div class="flyer-frame"></div>
</main>
</body>
</html>
```